Logo and packaging design for Lime restoration mortar

We need a logo and packaging design for out line of restoration profits. This includes labels for pales, and cement bags. I have attached out current logo. And a design from you that I really like. This is the kind of colour scheme and style I would like for our packaging.

I would like a new logo that is similar, or related to our existing but more presentable in a retail environment. I think a mark is also necessary for the logo. Currently it is just words and that makes branding a bit difficult.

Target Market(s)

DIYers we will be selling to hardware stores

Logo Text

Kelvane

Requirements
Must have
• Logo and packaging template that uses the new logo.
Nice to have
• I really like impactful logos. I love the crown logo, however I would prefer not to copy it. I would like a impactful logo, that can be easily broken down for branding different products.

```html
<!DOCTYPE html>
<html lang="en">
<head>
<meta charset="utf-8">
<title>Kelvane Lime Restoration Mortar – 50 kg Bag</title>
<link href="https://fonts.googleapis.com/css2?family=Raleway:wght@300;400;800;900&family=Oswald:wght@600&display=swap" rel="stylesheet">
<style>
  :root {
    --page: #ffffff;
    --purple: #652d90;
    --purple-soft: #9b7ab5;
    --charcoal: #39393b;
    --white: #ffffff;
    --gold: #e5c97a;
    --icon-lilac: #a98cc7;
  }
  * { margin: 0; padding: 0; box-sizing: border-box; }
  html, body {
    width: 1200px;
    height: 1200px;
    overflow: hidden;
    background: var(--page);
  }
  .canvas {
    position: relative;
    width: 1200px;
    height: 1200px;
    font-family: "Raleway", sans-serif;
  }
  .bag {
    position: absolute;
    left: 261px;
    top: 91px;
    width: 685px;
    height: 1026px;
  }
  .bag-shape {
    position: absolute;
    inset: 0;
  }
  .product-title {
    position: absolute;
    left: 0;
    width: 685px;
    text-align: center;
    line-height: 1;
  }
  .title-lime {
    top: 289px;
    left: -6px;
    font-weight: 900;
    font-size: 104px;
    color: var(--purple-soft);
    letter-spacing: -1px;
  }
  .title-restoration {
    top: 384px;
    left: 13px;
    font-weight: 900;
    font-size: 54px;
    color: var(--white);
    letter-spacing: -1px;
  }
  .title-mortar {
    top: 442px;
    left: 1px;
    font-weight: 300;
    font-size: 56px;
    color: var(--white);
    letter-spacing: 1px;
  }
  .brand {
    position: absolute;
    left: 61px;
    top: 772px;
    width: 200px;
    text-align: center;
  }
  .brand-dot {
    width: 96px;
    height: 96px;
    margin: 0 auto 46px;
    border-radius: 50%;
    background: var(--gold);
  }
  .brand-name {
    font-weight: 800;
    color: var(--white);
    font-size: 38px;
    line-height: 1.05;
    letter-spacing: 0.5px;
  }
  .brand-name span { display: block; font-size: 25px; letter-spacing: 1px; }
  .features {
    position: absolute;
    left: 486px;
    top: 786px;
    color: var(--white);
  }
  .feature {
    display: flex;
    align-items: center;
    gap: 10px;
    height: 48px;
    margin-bottom: 14px;
  }
  .feature svg { width: 36px; height: 46px; flex: none; }
  .feature-text {
    font-weight: 400;
    font-size: 18px;
    line-height: 1.1;
  }
  .net-weight {
    position: absolute;
    left: 492px;
    top: 916px;
    display: flex;
    align-items: flex-start;
    color: var(--purple-soft);
  }
  .net-weight-value {
    font-family: "Oswald", sans-serif;
    font-weight: 600;
    font-size: 52px;
    line-height: 1;
    letter-spacing: -1px;
  }
  .net-weight-unit {
    font-family: "Raleway", sans-serif;
    font-size: 17px;
    color: var(--white);
    margin: 2px 0 0 7px;
  }
</style>
</head>
<body>
<main class="canvas">
  <section class="bag">
    <svg class="bag-shape" viewBox="0 0 685 1026" aria-hidden="true">
      <rect width="685" height="1026" fill="var(--charcoal)"/>
      <polygon points="0,0 685,0 685,620 346,787 0,620" fill="var(--purple)"/>
    </svg>

    <h1>
      <span class="product-title title-lime">LIME</span>
      <span class="product-title title-restoration">RESTORATION</span>
      <span class="product-title title-mortar">MORTAR</span>
    </h1>

    <div class="brand">
      <div class="brand-dot"></div>
      <p class="brand-name">KELVANE<span>GROUP</span></p>
    </div>

    <ul class="features" style="list-style:none">
      <li class="feature">
        <svg viewBox="0 0 36 46" fill="none" stroke="var(--icon-lilac)" stroke-width="1.6" aria-hidden="true">
          <circle cx="18" cy="17" r="15"/>
          <circle cx="18" cy="17" r="10"/>
          <path d="M12 20 l1-6 3 3 2-4 2 4 3-3 1 6 z"/>
          <path d="M9 29 L4 41 L9 39 L11 44 L15 32"/>
          <path d="M27 29 L32 41 L27 39 L25 44 L21 32"/>
        </svg>
        <span class="feature-text">Premium<br>Quality</span>
      </li>
      <li class="feature">
        <svg viewBox="0 0 36 46" fill="none" stroke="var(--icon-lilac)" stroke-width="1.6" aria-hidden="true">
          <rect x="2" y="26" width="6" height="16" rx="1"/>
          <path d="M8 28 L14 28 L18 18 C19 15 23 16 22 20 L21 26 L31 26 C34 26 34 30 31 30 C34 30 34 34 31 34 C34 34 34 38 31 38 C33 38 33 42 30 42 L8 41"/>
          <path d="M26 4 l1.5 4 4 1.5 -4 1.5 -1.5 4 -1.5 -4 -4 -1.5 4 -1.5 z"/>
          <path d="M10 14 l1 2.5 2.5 1 -2.5 1 -1 2.5 -1 -2.5 -2.5 -1 2.5 -1 z"/>
          <path d="M32 16 l.8 1.8 1.8 .8 -1.8 .8 -.8 1.8 -.8 -1.8 -1.8 -.8 1.8 -.8 z"/>
        </svg>
        <span class="feature-text">Easy to<br>Use</span>
      </li>
    </ul>

    <p class="net-weight">
      <span class="net-weight-value">50</span>
      <span class="net-weight-unit">Kg</span>
    </p>
  </section>
</main>
</body>
</html>
```